Bramfield Animal Hospital brochure

We have found that our current clients do not know all of the services that we offer so we want to make a hospital brochure to make our services more known. Our website has all of our services listed but we find that clients aren't looking at our website as much as we would like so we are hoping a hospital brochure can sum up our main services and maybe lead to more people visiting our website. Our hospital colors are blue and maroon and our moto is "Outstanding Medicine, Extraordinary Service." Some of the service we would like to promote more include digital x-ray, ultrasounds, echocardiograms, laser therapy and dentals. We also offer after hours emergency care but only to our current clients. You can find more services listed on our website We are in a small town so we want a personal yet professional feel.

Feel free to visit our website to get a better feel for our business https://thecorvelpets.com/

• 6-8 panel brochure
• I included some photos from around the hospital. If you feel that you can make a few work in the brochure then great but don't feel obligated to.

```html
<!DOCTYPE html>
<html lang="en">
<head>
<meta charset="utf-8">
<title>Bramfield Animal Hospital – Brochure</title>
<link rel="stylesheet" href="https://fonts.googleapis.com/css2?family=Bebas+Neue&family=Montserrat:wght@400;500;600&display=swap">
<style>
  :root{
    --backdrop:#bdbdbd;
    --sheet:#0e0e0e;
    --sheet-soft:#161616;
    --white:#f2f2f2;
    --grey:#8c8c8c;
    --grey-dark:#5a5a5a;
    --maroon:#8e1d24;
    --fur-a:#2a2a2a;
    --fur-b:#050505;
    --cat-a:#8a7a66;
    --cat-b:#3b342c;
    --map-a:#cfe6d2;
    --map-b:#e9f1ea;
  }
  *{box-sizing:border-box;margin:0;padding:0}
  html,body{width:895px;height:1200px;overflow:hidden;background:var(--backdrop)}
  body{font-family:"Montserrat",sans-serif;color:var(--white)}
  .canvas{position:relative;width:895px;height:1200px}
  .spread{position:absolute;left:20px;width:855px;height:565px;display:flex;background:var(--sheet);box-shadow:0 6px 18px rgba(0,0,0,.35)}
  .spread--outside{top:20px}
  .spread--inside{top:615px}
  .panel{position:relative;width:285px;height:100%;overflow:hidden;border-right:1px solid #1f1f1f}
  .panel:last-child{border-right:none}
  .display{font-family:"Bebas Neue",sans-serif;line-height:.92;letter-spacing:.5px}

  /* outside – cover text panel */
  .motto{padding:34px 22px 0;text-align:center}
  .motto span{display:block}
  .motto .w1{font-size:50px;color:var(--white)}
  .motto .w2{font-size:64px;color:var(--grey)}
  .motto .w3{font-size:43px;color:var(--white)}
  .motto .w4{font-size:84px;color:var(--grey)}
  .brand{display:flex;align-items:center;justify-content:center;gap:7px;font-size:12px;font-weight:600;color:var(--white);letter-spacing:.3px}
  .brand-dot{width:14px;height:14px;border-radius:50%;background:var(--maroon);flex:none}
  .motto-panel .brand{margin-top:30px}
  .intro{padding:24px 22px 0;font-size:9.6px;line-height:1.55;text-align:justify;color:#d8d8d8}

  /* outside – contact panel */
  .contact-panel{text-align:center;background:linear-gradient(180deg,#262626 0%,var(--sheet) 35%)}
  .contact-panel .brand{margin-top:70px}
  .contact-icons{display:flex;justify-content:center;gap:4px;margin-top:70px}
  .contact-lines{margin-top:8px;font-size:10.5px;line-height:1.55}
  .map{width:200px;height:200px;margin:42px auto 0;border-radius:50%;border:5px solid #e8e8e8;background:linear-gradient(135deg,var(--map-a),var(--map-b))}

  /* outside – back photo panel */
  .photo{position:absolute}
  .dog-portrait{inset:0;background:radial-gradient(ellipse at 70% 40%,var(--fur-a) 0%,#121212 45%,var(--fur-b) 80%)}
  .back-panel .brand{position:absolute;left:0;right:0;bottom:46px}

  /* inside – services */
  .services{padding:30px 14px 0 16px}
  .services h2{font-family:"Bebas Neue",sans-serif;font-weight:400;font-size:27px;color:var(--grey);letter-spacing:.5px;margin-bottom:14px}
  .service-list{display:grid;grid-template-columns:1fr 1fr;column-gap:8px;row-gap:13px;list-style:none}
  .service{display:flex;align-items:center;gap:6px;font-size:9.2px;line-height:1.15;color:#e4e4e4}
  .service-icon{flex:none;width:22px;height:22px;border-radius:50%;border:1px solid #9a9a9a;display:flex;align-items:center;justify-content:center}
  .service-icon::after{content:"";width:7px;height:7px;border-radius:50%;background:#9a9a9a}

  /* inside – promise */
  .promise{padding:34px 14px 0;text-align:center}
  .promise span{display:block}
  .promise .p1{font-size:58px;color:var(--white)}
  .promise .p2{font-size:78px;color:var(--grey)}
  .promise .p3{font-size:56px;color:var(--white)}
  .kitten{left:40px;right:40px;bottom:0;height:260px;border-radius:40% 40% 0 0;background:radial-gradient(ellipse at 50% 45%,var(--cat-a) 0%,var(--cat-b) 55%,var(--sheet) 85%)}

  /* inside – emergency */
  .emergency-panel{background:var(--sheet-soft)}
  .dog-resting{left:0;right:0;top:0;height:180px;background:radial-gradient(ellipse at 50% 60%,#6d6d6d 0%,#262626 45%,var(--sheet-soft) 80%)}
  .cat-playing{left:0;right:0;bottom:0;height:160px;background:radial-gradient(ellipse at 55% 55%,var(--cat-a) 0%,var(--cat-b) 45%,var(--sheet-soft) 80%)}
  .emergency{position:absolute;left:20px;right:20px;top:175px}
  .emergency .h1{font-size:66px;color:var(--white)}
  .emergency .h2{font-size:33px;color:var(--white);margin-top:2px}
  .emergency p{margin-top:12px;font-size:9.4px;line-height:1.5;text-align:justify;color:#dcdcdc}
</style>
</head>
<body>
<main class="canvas">

  <section class="spread spread--outside">
    <article class="panel motto-panel">
      <h1 class="motto display">
        <span class="w1">Outstanding</span>
        <span class="w2">Medicine</span>
        <span class="w3">Extraordinary</span>
        <span class="w4">Service</span>
      </h1>
      <div class="brand"><span class="brand-dot"></span>Bramfield Animal Hospital</div>
      <p class="intro">We built Bramfield Animal Hospital for you. It is so important to us that you can walk into an environment where you feel you are always put first, and where the little things have been thought of to make this a truly wonderful experience. We want to make your life easier. We offer evening hours, drop-offs, and house call appointments. And existing clients get access to 24 hour emergency care. Because we are always looking out for you.</p>
    </article>

    <article class="panel contact-panel">
      <div class="brand"><span class="brand-dot"></span>Bramfield Animal Hospital</div>
      <div class="contact-icons" aria-hidden="true">
        <svg width="12" height="12" viewBox="0 0 12 12"><circle cx="6" cy="6" r="5.4" fill="none" stroke="#f2f2f2"/><path d="M4 3.2l1 1.4-.6.8a4 4 0 0 0 1.8 1.8l.8-.6 1.4 1-.6 1.2C5.6 8.6 3.4 6.4 3 4z" fill="#f2f2f2"/></svg>
        <svg width="12" height="12" viewBox="0 0 12 12"><circle cx="6" cy="6" r="5.4" fill="none" stroke="#f2f2f2"/><rect x="3" y="4" width="6" height="4" fill="none" stroke="#f2f2f2" stroke-width=".8"/><path d="M3 4l3 2.2L9 4" fill="none" stroke="#f2f2f2" stroke-width=".8"/></svg>
        <svg width="12" height="12" viewBox="0 0 12 12"><circle cx="6" cy="6" r="5.4" fill="none" stroke="#f2f2f2"/><circle cx="6" cy="6" r="3" fill="none" stroke="#f2f2f2" stroke-width=".8"/><path d="M3 6h6M6 3v6" stroke="#f2f2f2" stroke-width=".6"/></svg>
      </div>
      <div class="contact-lines">
        <div>802-555-0148</div>
        <div>info@thecorvelpets.com</div>
        <div>https://thecorvelpets.com/</div>
      </div>
      <div class="map" role="img" aria-label="Street map showing the hospital location"></div>
    </article>

    <article class="panel back-panel">
      <div class="photo dog-portrait" role="img" aria-label="Black Labrador portrait emerging from a dark background"></div>
      <div class="brand"><span class="brand-dot"></span>Bramfield Animal Hospital</div>
    </article>
  </section>

  <section class="spread spread--inside">
    <article class="panel services">
      <h2>Services We Offer</h2>
      <ul class="service-list">
        <li class="service"><span class="service-icon"></span>Cardiology Care</li>
        <li class="service"><span class="service-icon"></span>Flea and Tick Prevention</li>
        <li class="service"><span class="service-icon"></span>Cold Laser Therapy</li>
        <li class="service"><span class="service-icon"></span>Heartworm Preventative</li>
        <li class="service"><span class="service-icon"></span>Digital X-Ray</li>
        <li class="service"><span class="service-icon"></span>In-House Laboratory</li>
        <li class="service"><span class="service-icon"></span>Emergency Care</li>
        <li class="service"><span class="service-icon"></span>Microchipping</li>
        <li class="service"><span class="service-icon"></span>End-Of-Life Care</li>
        <li class="service"><span class="service-icon"></span>Nutritional Consultations</li>
        <li class="service"><span class="service-icon"></span>Parasite Testing</li>
        <li class="service"><span class="service-icon"></span>Puppy and Kitten Care</li>
        <li class="service"><span class="service-icon"></span>Allergy and Dermatology</li>
        <li class="service"><span class="service-icon"></span>Blood Tests and Urine Screening</li>
        <li class="service"><span class="service-icon"></span>Avian Care</li>
        <li class="service"><span class="service-icon"></span>Canine and Feline Dental Care</li>
        <li class="service"><span class="service-icon"></span>Senior Wellness</li>
        <li class="service"><span class="service-icon"></span>Soft Tissue Surgery</li>
        <li class="service"><span class="service-icon"></span>Vaccinations Process</li>
        <li class="service"><span class="service-icon"></span>Wellness Exams</li>
      </ul>
    </article>

    <article class="panel promise-panel">
      <h2 class="promise display">
        <span class="p1">Every</span>
        <span class="p2">Petient</span>
        <span class="p3">Everytime</span>
      </h2>
      <div class="photo kitten" role="img" aria-label="Tabby kitten sitting"></div>
    </article>

    <article class="panel emergency-panel">
      <div class="photo dog-resting" role="img" aria-label="Border collie lying on dark fur"></div>
      <div class="photo cat-playing" role="img" aria-label="Tabby cat lying on its back, playing"></div>
      <div class="emergency">
        <h2 class="display"><span class="h1">24 Hour</span><br><span class="h2">Emergency Care</span></h2>
        <p>We keep a veterinarian on call 24 hours a day for emergency services, in order to treat your pet as quickly as possible. We restrict after hours emergency care to current clients. If you are not a current client and may be experiencing an after hours pet emergency, please contact your regular veterinarian or Hillcrest Animal Emergency Clinic at (518) 555-0172.</p>
      </div>
    </article>
  </section>

</main>
</body>
</html>
```